New Webpage for High Class Expert Witness Services Company

We are looking for a minimalist design for a webpage that just has our logo and an entry form offer to connect with one of our Liaisons.
The entry form should just ask for Name, Email, Contact Info and Description of Project.

Company Name is: The Marlow Crest Advisory Services

Number of Pages Required

1 page

```html
<!DOCTYPE html>
<html lang="en">
<head>
<meta charset="utf-8">
<title>The Marlow Crest Advisory Services — Connect With a Liaison</title>
<link href="https://fonts.googleapis.com/css2?family=Marcellus&family=Outfit:wght@400;600&display=swap" rel="stylesheet">
<style>
  :root {
    --page-dark: #141414;
    --page-mid: #262420;
    --brand-silver: #d9d9d9;
    --card-cream: #fdf9ee;
    --field-grey: #ebebeb;
    --ink: #0b0b0b;
    --placeholder: #4a4a4a;
    --white: #ffffff;
  }
  * { box-sizing: border-box; margin: 0; padding: 0; }
  html, body { width: 1200px; height: 788px; overflow: hidden; }
  body {
    position: relative;
    background: var(--page-dark);
    font-family: "Outfit", sans-serif;
  }
  .hero-backdrop {
    position: absolute; inset: 0;
    background:
      radial-gradient(ellipse 260px 420px at 110px 420px, #2a2824 0%, transparent 100%),
      radial-gradient(ellipse 260px 420px at 1090px 420px, #2a2824 0%, transparent 100%),
      linear-gradient(180deg, var(--page-dark) 0%, var(--page-mid) 55%, var(--page-dark) 100%);
  }
  .brand {
    position: absolute; top: 64px; left: 0; width: 100%;
    display: flex; justify-content: center; align-items: center; gap: 12px;
    color: var(--brand-silver);
    font-family: "Marcellus", serif; font-size: 30px; line-height: 34px;
  }
  .brand-mark { width: 14px; height: 14px; background: var(--brand-silver); }
  .contact-card {
    position: absolute; left: 342px; top: 190px; width: 516px; height: 528px;
    background: var(--card-cream); border-radius: 27px;
    padding: 41px 39px 0;
  }
  .contact-title {
    font-family: "Marcellus", serif; font-weight: 400;
    font-size: 37px; line-height: 37px; text-align: center; color: var(--ink);
    letter-spacing: -0.5px;
  }
  .contact-form { margin-top: 26px; display: flex; flex-direction: column; gap: 10px; }
  .field {
    position: relative; height: 45px; border-radius: 23px;
    background: var(--field-grey);
    display: flex; align-items: center; padding-left: 44px;
    font-size: 12px; color: var(--placeholder);
  }
  .field-message { height: 118px; align-items: flex-start; padding-top: 13px; }
  .field svg { position: absolute; left: 22px; width: 11px; height: 11px; fill: #2b2b2b; }
  .field-message svg { top: 14px; }
  .submit-button {
    position: relative; height: 45px; border: 0; border-radius: 23px;
    background: var(--ink); color: var(--white);
    font-family: "Outfit", sans-serif; font-weight: 600; font-size: 13px;
    display: flex; align-items: center; justify-content: center;
  }
  .submit-button svg { position: absolute; right: 23px; width: 15px; height: 15px; fill: var(--white); }
</style>
</head>
<body>
  <div class="hero-backdrop" role="img" aria-label="Dark photograph of armed soldiers in silhouette on both sides"></div>

  <header class="brand">
    <span class="brand-mark"></span>
    <span class="brand-name">The Marlow Crest Advisory Services</span>
  </header>

  <section class="contact-card">
    <h1 class="contact-title">Connect With a Liaison<br>For Your Project</h1>
    <form class="contact-form">
      <div class="field">
        <svg viewBox="0 0 16 16"><circle cx="8" cy="4.5" r="3.5"/><path d="M1 16c0-4 3-6.5 7-6.5s7 2.5 7 6.5z"/></svg>
        First name
      </div>
      <div class="field">
        <svg viewBox="0 0 16 16"><path d="M0 3h16v1.5L8 9 0 4.5z"/><path d="M0 6.3l8 4.5 8-4.5V13H0z"/></svg>
        Email
      </div>
      <div class="field">
        <svg viewBox="0 0 16 16"><path d="M3.5 0.5l3 3.2-1.7 2c1 2 2.5 3.5 4.5 4.5l2-1.7 3.2 3-2 3C6 14 2 10 0.5 2.5z"/></svg>
        Phone Number
      </div>
      <div class="field field-message">
        <svg viewBox="0 0 16 16"><ellipse cx="9.5" cy="6.5" rx="6.5" ry="5.5"/><path d="M5 10l-2 4 5-3z"/><circle cx="3" cy="9" r="2.6"/></svg>
        Message
      </div>
      <button type="button" class="submit-button">
        Submit Now
        <svg viewBox="0 0 16 16"><path d="M16 0L0 7l5 2 9-7-7 8v6l3-4 4 2z"/></svg>
      </button>
    </form>
  </section>
</body>
</html>
```